Business Cards for a unique Russian patisserie

ORLU Golden Bakes bakery intends to introduce Australian public to amazing Russian pastries and traditions of genuine Russian hospitality.
ORLU business model is a café, selling a mix of Russian, Eastern European and traditional pastries produced in-house.
ORLU’s ultimate goal is to create a superior eating experience and to become a destination eatery in Sydney.
I would like the business cards match our ambitious purpose, to be unique and bold. I want them to be sophisticated (as opposed to straightforward and tacky) and graphical. I would love if Russian national ornament (hohloma) elements to be used.
Dominating colours - red and black. For the styling guide please see our logo attached.
Target Market(s)
Business partners, suppliers, possible corporate clients
Industry/Entity Type
Bakery
Look and feel

```html
<!DOCTYPE html>
<html lang="en">
<head>
<meta charset="utf-8">
<title>ORLU Golden Bakes – Business Cards</title>
<link rel="stylesheet" href="https://fonts.googleapis.com/css2?family=Source+Sans+3:wght@400;600;700&display=swap">
<style>
  :root {
    --page: #efeae4;
    --card: #ffffff;
    --red: #e51e26;
    --brown: #3a2417;
    --ink: #1f1f1f;
    --cream: #f7efd6;
    --rule: #c9c9c9;
  }
  * { box-sizing: border-box; margin: 0; padding: 0; }
  html, body {
    width: 1200px; height: 1192px; overflow: hidden;
    background: var(--page);
    font-family: "Source Sans 3", Arial, sans-serif;
  }
  .canvas { position: relative; width: 1200px; height: 1192px; }

  .card {
    position: absolute;
    width: 923px; height: 531px;
    border-radius: 26px;
    overflow: hidden;
    box-shadow: 0 2px 6px rgba(0,0,0,.18);
  }
  .card--front { left: 250px; top: 49px; background: var(--card); }
  .card--back  { left: 50px;  top: 618px; background: var(--red); }

  .wordmark {
    position: absolute;
    text-align: center;
    font-weight: 700;
    line-height: 1;
  }
  .card--front .wordmark {
    left: 60px; top: 150px; width: 400px;
    color: var(--brown);
    font-size: 96px; letter-spacing: 4px;
  }
  .wordmark .wordmark__sub {
    display: block;
    font-size: 30px; letter-spacing: 1px;
    margin-top: 12px;
  }

  .divider {
    position: absolute; left: 497px; top: 95px;
    width: 2px; height: 245px;
    background: linear-gradient(var(--rule), #8f8f8f, var(--rule));
  }

  .contacts { position: absolute; left: 526px; top: 92px; list-style: none; }
  .contacts li {
    display: flex; align-items: center; gap: 8px;
    font-size: 22px; color: var(--ink); height: 36.5px;
  }
  .contacts svg { width: 18px; height: 18px; fill: var(--red); flex: none; }

  .address {
    position: absolute; left: 526px; top: 262px;
    font-size: 21px; line-height: 34px; color: var(--ink);
  }

  .waves { position: absolute; left: 0; top: 0; width: 923px; height: 531px; }

  .holder {
    position: absolute; left: 608px; top: 444px; width: 260px;
    text-align: center; color: #fff;
  }
  .holder__name  { font-size: 32px; font-weight: 700; line-height: 1; }
  .holder__title { font-size: 25px; font-weight: 400; line-height: 1; margin-top: 6px; }

  .card--back .wordmark {
    left: 0; top: 190px; width: 923px;
    color: var(--cream);
    font-size: 110px; letter-spacing: 6px;
  }
  .card--back .wordmark .wordmark__sub { font-size: 34px; margin-top: 14px; }

  .back-url {
    position: absolute; left: 0; top: 458px; width: 923px;
    text-align: center; color: #fff;
    font-size: 27px; letter-spacing: 5px;
  }
</style>
</head>
<body>
<main class="canvas">

  <section class="card card--front" aria-label="Business card front">
    <svg class="waves" viewBox="0 0 923 531" aria-hidden="true">
      <path d="M200 531 C380 470 560 420 923 400 L923 531 Z" fill="var(--brown)"/>
      <path d="M0 478 C220 458 480 405 923 382" fill="none" stroke="var(--brown)" stroke-width="9"/>
      <path d="M0 482 C180 495 330 472 480 440 C360 490 220 531 0 531 Z" fill="var(--red)"/>
      <path d="M0 500 C200 505 340 475 480 440" fill="none" stroke="#fff" stroke-width="6"/>
    </svg>

    <div class="wordmark">ORLU<span class="wordmark__sub">Golden Bakes</span></div>

    <div class="divider"></div>

    <ul class="contacts">
      <li>
        <svg viewBox="0 0 20 20"><path d="M4 2h4l2 5-3 2a11 11 0 0 0 4 4l2-3 5 2v4a2 2 0 0 1-2 2A16 16 0 0 1 2 4a2 2 0 0 1 2-2z"/></svg>
        012-345-6789
      </li>
      <li>
        <svg viewBox="0 0 20 20"><path d="M2 8h16v8h-3v-3H5v3H2zM4 4h12v3H4z"/></svg>
        012-345-6789
      </li>
      <li>
        <svg viewBox="0 0 20 20"><path d="M2 5h16v11H2zM3 6l7 6 7-6" stroke="#fff" stroke-width="1.5"/></svg>
        info@orlubakes.com
      </li>
      <li>
        <svg viewBox="0 0 20 20"><circle cx="10" cy="10" r="8"/><path d="M2 10h16M10 2c-4 4-4 12 0 16M10 2c4 4 4 12 0 16" stroke="#fff" stroke-width="1.3" fill="none"/></svg>
        www.orlubakes.com
      </li>
    </ul>

    <p class="address">Street Name, City Name<br>Zip Code-00000</p>

    <div class="holder">
      <p class="holder__name">Your Name</p>
      <p class="holder__title">Title</p>
    </div>
  </section>

  <section class="card card--back" aria-label="Business card back">
    <div class="wordmark">ORLU<span class="wordmark__sub">Golden Bakes</span></div>
    <p class="back-url">www.orlubakes.com</p>
  </section>

</main>
</body>
</html>
```